Business card

would like a double sided business card made up with my logos provided.
Prefer card to have black background and to use the black logos, with matching blue writing for the text.
One side to just be the logo, (Try to use both the black logos)
the other side to have the logo and also my credentials/business information.

Covering all aspects of Carpentry and Building Services

Marcus Thelwin
Qualified Carpenter
Mob: 0417263985
Email: rkt.joinery@fernmail.example
ABN: 47 619 283 504

Industry/Entity Type

Business

Contact Information for Business Card

Marcus Thelwin
Qualified Carpenter
Mob: 0417263985
ABN: 47 619 283 504

Requirements
Must have
• Please try to use both the black logos and incorporate into the card.

```html
<!DOCTYPE html>
<html lang="en">
<head>
<meta charset="utf-8">
<title>RKT Joinery – Business Card</title>
<link rel="stylesheet" href="https://fonts.googleapis.com/css2?family=Questrial&display=swap">
<style>
  :root {
    --ink: #2b2b2d;
    --blue: #1e8fd6;
    --grey: #8a8a8c;
    --paper: #ffffff;
    --backdrop: #3a3230;
  }
  * { margin: 0; padding: 0; box-sizing: border-box; }
  html, body {
    width: 1200px; height: 716px; overflow: hidden;
    background: var(--backdrop);
    font-family: "Questrial", "Century Gothic", sans-serif;
  }
  .canvas {
    position: relative; width: 1200px; height: 716px;
    display: flex; align-items: center; justify-content: center; gap: 60px;
  }
  .card {
    position: relative; width: 510px; height: 300px;
    background: var(--paper);
    box-shadow: 0 10px 30px rgba(0,0,0,.45);
    overflow: hidden;
  }
  /* Front */
  .card--front {
    display: flex; flex-direction: column; align-items: center; justify-content: center;
  }
  .brand-mark { display: flex; align-items: center; gap: 14px; }
  .brand-mark__square { width: 34px; height: 34px; background: var(--blue); }
  .brand-name {
    color: var(--ink); font-size: 62px; letter-spacing: 6px; line-height: 1;
  }
  .brand-tagline {
    margin-top: 14px; color: var(--grey);
    font-size: 17px; letter-spacing: 4px; text-transform: uppercase;
  }
  /* Back */
  .card--back .brand {
    position: absolute; top: 38px; right: 34px; text-align: right;
  }
  .card--back .brand-name { font-size: 40px; letter-spacing: 4px; }
  .card--back .brand-mark__square { width: 24px; height: 24px; }
  .card--back .brand-tagline {
    margin-top: 8px; color: var(--blue); font-size: 11px; letter-spacing: 3.5px;
  }
  .holder { position: absolute; left: 36px; top: 166px; }
  .holder__name { color: var(--ink); font-size: 19px; }
  .holder__role { color: var(--blue); font-size: 15px; margin-top: 3px; }
  .contact {
    position: absolute; left: 250px; top: 176px;
    list-style: none; font-size: 13.5px; line-height: 1.55; color: var(--ink);
  }
  .contact__label { color: var(--blue); }
  .card__band {
    position: absolute; left: 0; right: 0; bottom: 0; height: 22px;
    background: var(--blue);
  }
</style>
</head>
<body>
<main class="canvas">
  <section class="card card--front" aria-label="Business card front">
    <div class="brand-mark">
      <span class="brand-mark__square"></span>
      <span class="brand-name">RKT JOINERY</span>
    </div>
    <p class="brand-tagline">Carpenters and Builders</p>
  </section>

  <section class="card card--back" aria-label="Business card back">
    <div class="brand">
      <div class="brand-mark">
        <span class="brand-mark__square"></span>
        <span class="brand-name">RKT JOINERY</span>
      </div>
      <p class="brand-tagline">Carpenters and Builders</p>
    </div>
    <div class="holder">
      <p class="holder__name">Marcus Thelwin</p>
      <p class="holder__role">Qualified Carpenter</p>
    </div>
    <ul class="contact">
      <li><span class="contact__label">Mob:</span> 0417263985</li>
      <li><span class="contact__label">Email:</span> rkt.joinery@fernmail.example</li>
      <li><span class="contact__label">ABN:</span> 47 619 283 504</li>
    </ul>
    <div class="card__band"></div>
  </section>
</main>
</body>
</html>
```